Stationery Design Project

I have recently had developed a logo for my new company Northbay Venture Partners -see logo attached.
I now need the following
1. Letterhead design as Word template
text needs to show the logo and then
Northbay Venture Partners Pty Ltd
ABN 83 402 615 938
Level 5, Arbour House
17 Pellmont Place
Harrowdene, NSW 2768
Tel: + 61(0)2 9374 2816
www.northbayventurepartners.com
lucasd@northbayventurepartners.com
2. Business card -print ready -
Front side needs to show logo then text as follows
Lucas Drayton
CEO
Level 5, Arbour House
17 Pellmont Place
Harrowdene, NSW 2768
T: + 61 (0)2 9374 2816
M: + 61 (0)438 721 604
lucasd@pelvarogroup.com.au
On the back of the business card should appear the logo then text as follows
Correct text for the back of the card now in the attached word file please use bold and italics as indicated. Thanks
3. With compliments slip: Including logo + the web address www.northbayventurepartners.com
With compliments slip should fit 3 to an A4 sheet
4. Envelop design including logo + address
For the ethos of the company original brief for the logo below:
I am creating a new business advisory company called Northbay Venture Partners. the Web address will be www.northbayventurepartners.com This business is focused on assisting medium size businesses to achieve their growth objectives. The three pillars are self explanatory -it is focused on businesses that seek to build a global footprint, they seek to define/refine their business model and strategy, they are forward looking and focused on achieving growth.
The ethos of this company will be innovative thinking, passionate, dynamic, entrepreneurial this should reflected in the logo. That said the Logo should not be 'complicated' it should be simple and elegant...
Thanks Lucas Drayton
Reason: I have been travelling all this week -so will only get a chance to review this weekend. Thanks
Target Market(s)
Medium sized business owners with sales between US$5m and $50m.
Industry/Entity Type
Business
Look and feel

```html
<!DOCTYPE html>
<html lang="en">
<head>
<meta charset="utf-8">
<title>Northbay Venture Partners – Business Card</title>
<link rel="stylesheet" href="https://fonts.googleapis.com/css2?family=Jost:wght@400;500;600&display=swap">
<style>
  :root {
    --bg: #ececec;
    --card: #ffffff;
    --navy: #003478;
    --name-navy: #0d3a82;
    --brand-blue: #0a63b5;
    --teal: #74c4c5;
    --ink: #222a33;
    --rule: #3a3a3a;
  }
  * { box-sizing: border-box; margin: 0; padding: 0; }
  html, body { width: 1200px; height: 900px; overflow: hidden; }
  body {
    background: var(--bg);
    font-family: "Jost", "Helvetica Neue", Arial, sans-serif;
    color: var(--ink);
    position: relative;
  }
  .card {
    position: absolute;
    width: 638px;
    height: 355px;
    background: var(--card);
    box-shadow: 3px 4px 6px rgba(0,0,0,0.22);
    overflow: hidden;
  }
  .card-front { left: 101px; top: 69px; }
  .card-back { left: 451px; top: 466px; }

  .brand {
    position: absolute;
    display: flex;
    align-items: center;
    gap: 8px;
    color: var(--brand-blue);
    font-weight: 500;
    white-space: nowrap;
    line-height: 1;
  }
  .brand-mark {
    display: block;
    width: 30px;
    height: 30px;
    background: var(--teal);
  }
  .card-front .brand { left: 20px; top: 36px; font-size: 43px; }
  .card-back .brand { left: 22px; top: 36px; font-size: 46px; }

  .person-name {
    position: absolute;
    left: 21px; top: 101px;
    font-size: 24px;
    font-weight: 600;
    color: var(--name-navy);
  }
  .person-title {
    position: absolute;
    left: 21px; top: 131px;
    font-size: 21px;
    color: var(--name-navy);
  }
  .contact-list {
    position: absolute;
    left: 21px; top: 164px;
    width: 482px;
    list-style: none;
    font-size: 18px;
  }
  .contact-row {
    height: 35px;
    display: flex;
    align-items: center;
    gap: 6px;
    border-bottom: 1.3px solid var(--rule);
    white-space: nowrap;
  }
  .contact-row:last-child { border-bottom: none; }
  .contact-row.indent { padding-left: 20px; }
  .icon { width: 13px; height: 13px; fill: var(--navy); flex: none; }
  .sep { margin: 0 5px; }

  .services {
    position: absolute;
    left: 0; top: 108px;
    width: 100%;
    list-style: none;
  }
  .service {
    height: 40px;
    padding-left: 71px;
    display: flex;
    align-items: center;
    gap: 7px;
    font-size: 21px;
    color: #ffffff;
    background: var(--navy);
  }
  .service::before {
    content: "";
    width: 5px;
    height: 5px;
    border-radius: 50%;
    background: currentColor;
    flex: none;
  }
  .service:nth-child(even) { background: var(--teal); color: var(--ink); }
  .service:nth-child(5) { height: 36px; }
  .service:last-child { height: 51px; padding-bottom: 12px; }
</style>
</head>
<body>

<section class="card card-front" aria-label="Business card front">
  <div class="brand"><span class="brand-mark"></span>Northbay Venture Partners</div>
  <div class="person-name">Lucas Drayton</div>
  <div class="person-title">CEO</div>
  <ul class="contact-list">
    <li class="contact-row">
      <svg class="icon" viewBox="0 0 12 12"><rect x="3" y="0" width="6" height="12" rx="1"/><rect x="4" y="2" width="4" height="6" fill="#fff"/></svg>
      + 61 438 721 604<span class="sep">|</span>
      <svg class="icon" viewBox="0 0 12 12"><path d="M3 1 L5 3 L4 5 Q5 7 7 8 L9 7 L11 9 L9 11 Q3 10 1 3 Z"/></svg>
      + 61 (0)2 9374 2816
    </li>
    <li class="contact-row">
      <svg class="icon" viewBox="0 0 12 12"><rect x="3" y="0" width="6" height="4"/><rect x="0" y="4" width="12" height="5" rx="1"/><rect x="3" y="8" width="6" height="4"/></svg>
      + 61 (0)2 4719 3065<span class="sep">|</span>
      <svg class="icon" viewBox="0 0 12 12"><rect x="0" y="2" width="12" height="8"/><path d="M0 2 L6 7 L12 2" stroke="#fff" stroke-width="1" fill="none"/></svg>
      lucasd@pelvarogroup.com.au
    </li>
    <li class="contact-row">
      <svg class="icon" viewBox="0 0 12 12"><path d="M6 0 L12 6 L10 6 L10 12 L7 12 L7 8 L5 8 L5 12 L2 12 L2 6 L0 6 Z"/></svg>
      Northbay Venture Partners Pty Ltd<span class="sep">|</span>Level 3, Arbour House
    </li>
    <li class="contact-row indent">17 Pellmont Place<span class="sep">|</span>Harrowdene, NSW 2768</li>
    <li class="contact-row">
      <svg class="icon" viewBox="0 0 12 12"><circle cx="6" cy="6" r="6"/><path d="M0 6 H12 M6 0 V12 M2 2.5 Q6 5 10 2.5 M2 9.5 Q6 7 10 9.5" stroke="#fff" stroke-width="0.8" fill="none"/></svg>
      www.northbayventurepartners.com
    </li>
  </ul>
</section>

<section class="card card-back" aria-label="Business card back">
  <div class="brand"><span class="brand-mark"></span>Northbay Venture Partners</div>
  <ul class="services">
    <li class="service">Develop the Right Strategy for your business</li>
    <li class="service">Be accountable - create your Advisory Board</li>
    <li class="service">Build a Business Plan your team will implement</li>
    <li class="service">Take your business global - Export Market Development</li>
    <li class="service">CEO groups</li>
    <li class="service">Presentations, Seminars, Conferences</li>
  </ul>
</section>

</body>
</html>
```